PHD-project

i need the figures to be in the same stile. info is inside the file. There are 5 figures that need redesign. this is for PhD.

Target Market(s)

it will be used in my phd

Colors

Designer to choose colors to be used in the design.

```html
<!DOCTYPE html>
<html lang="en">
<head>
<meta charset="utf-8">
<title>Research Overview Diagram</title>
<link rel="stylesheet" href="https://fonts.googleapis.com/css2?family=Montserrat:wght@400;500;600;700&display=swap">
<style>
  :root {
    --panel: #5b93b0;
    --panel-line: #7fb0c9;
    --deep: #2f7098;
    --deeper: #1f6189;
    --accent: #62a7cc;
    --navy: #0f4670;
    --paper-ref: #1a4b78;
    --header-text: #6b6b6b;
    --white: #ffffff;
    --pink: #e07a95;
    --green: #78b560;
    --orange: #f5b25a;
    --sky: #5bbbe8;
    --purple: #8e58a8;
    --periwinkle: #6f8fcf;
  }
  html, body { margin: 0; padding: 0; width: 1200px; height: 679px; overflow: hidden; background: var(--white); }
  .diagram { display: block; width: 1200px; height: 679px; font-family: "Montserrat", sans-serif; }
  .header-label { fill: var(--header-text); font-size: 17px; font-weight: 500; text-anchor: middle; }
  .cell-text { fill: var(--white); font-size: 12px; font-weight: 500; text-anchor: middle; }
  .cell-note { fill: #d4e6f0; font-size: 10px; font-weight: 400; text-anchor: middle; }
  .paper-ref { fill: var(--paper-ref); font-size: 12px; font-weight: 500; text-anchor: middle; }
  .lead { fill: #b9d6e6; font-size: 11px; font-weight: 400; text-anchor: middle; }
  .strong { fill: var(--white); font-size: 13px; font-weight: 700; text-anchor: middle; }
  .soft { fill: #cfe3ee; font-size: 11px; font-weight: 400; text-anchor: middle; }
  .rtd { fill: var(--accent); font-size: 29px; font-weight: 500; text-anchor: middle; }
  .dimension { fill: var(--accent); font-size: 11px; font-weight: 500; text-anchor: middle; }
  .cap-label { fill: var(--accent); font-size: 11px; font-weight: 500; }
  .divider { stroke: var(--panel-line); stroke-width: 1; }
  .link { fill: none; stroke-width: 1.2; stroke-linejoin: round; }
  .dot { stroke: var(--white); stroke-width: 1.5; }
</style>
</head>
<body>
<svg class="diagram" viewBox="0 0 1200 679" xmlns="http://www.w3.org/2000/svg">
  <defs>
    <linearGradient id="header-fade" x1="0" y1="0" x2="0" y2="1">
      <stop offset="0" stop-color="#e6e6e6"/>
      <stop offset="1" stop-color="#ffffff"/>
    </linearGradient>
    <marker id="tip-pink" viewBox="0 0 6 6" refX="6" refY="3" markerWidth="5" markerHeight="5" orient="auto"><path d="M0 0 L6 3 L0 6 Z" fill="var(--pink)"/></marker>
    <marker id="tip-green" viewBox="0 0 6 6" refX="6" refY="3" markerWidth="5" markerHeight="5" orient="auto"><path d="M0 0 L6 3 L0 6 Z" fill="var(--green)"/></marker>
    <marker id="tip-orange" viewBox="0 0 6 6" refX="6" refY="3" markerWidth="5" markerHeight="5" orient="auto"><path d="M0 0 L6 3 L0 6 Z" fill="var(--orange)"/></marker>
    <marker id="tip-sky" viewBox="0 0 6 6" refX="6" refY="3" markerWidth="5" markerHeight="5" orient="auto"><path d="M0 0 L6 3 L0 6 Z" fill="var(--sky)"/></marker>
    <marker id="tip-purple" viewBox="0 0 6 6" refX="6" refY="3" markerWidth="5" markerHeight="5" orient="auto"><path d="M0 0 L6 3 L0 6 Z" fill="var(--purple)"/></marker>
    <marker id="tip-periwinkle" viewBox="0 0 6 6" refX="6" refY="3" markerWidth="5" markerHeight="5" orient="auto"><path d="M0 0 L6 3 L0 6 Z" fill="var(--periwinkle)"/></marker>
    <marker id="tip-navy" viewBox="0 0 6 6" refX="5" refY="3" markerWidth="6" markerHeight="6" orient="auto-start-reverse"><path d="M0 0 L6 3 L0 6 Z" fill="var(--navy)"/></marker>
  </defs>

  <!-- Column headers -->
  <g class="headers">
    <rect x="61" y="88" width="183" height="46" rx="8" fill="url(#header-fade)"/>
    <text class="header-label" x="153" y="113">Poitioning</text>
    <text class="header-label" x="153" y="133">The Research</text>
    <rect x="290" y="88" width="183" height="46" rx="8" fill="url(#header-fade)"/>
    <text class="header-label" x="382" y="113">Research</text>
    <text class="header-label" x="382" y="133">Approach</text>
    <rect x="589" y="88" width="131" height="46" rx="8" fill="url(#header-fade)"/>
    <text class="header-label" x="654" y="113">Methods</text>
    <rect x="799" y="88" width="131" height="46" rx="8" fill="url(#header-fade)"/>
    <text class="header-label" x="865" y="113">Findings</text>
    <rect x="1012" y="88" width="131" height="46" rx="8" fill="url(#header-fade)"/>
    <text class="header-label" x="1077" y="113">Contribution</text>
  </g>

  <!-- Positioning: nested ellipses -->
  <g class="positioning">
    <ellipse cx="154" cy="264" rx="59" ry="90" fill="var(--panel)"/>
    <ellipse cx="154" cy="449" rx="76" ry="133" fill="var(--panel)"/>
    <ellipse cx="154" cy="302" rx="44" ry="58" fill="var(--deep)"/>
    <ellipse cx="154" cy="401" rx="63" ry="85" fill="var(--deep)"/>
    <ellipse cx="154" cy="302" rx="44" ry="58" fill="var(--deeper)" opacity="0.35"/>
    <text class="lead" x="154" y="210">Design</text>
    <text class="strong" x="154" y="227">Thinking</text>
    <text class="lead" x="154" y="281">Design</text>
    <text class="strong" x="154" y="298">Practice</text>
    <text class="strong" x="154" y="386">Theoretical</text>
    <text class="strong" x="154" y="401">Approach</text>
    <text class="soft" x="154" y="420">to Building</text>
    <text class="soft" x="154" y="433">Design Thinking</text>
    <text class="soft" x="154" y="446">Capability</text>
    <text class="lead" x="154" y="506">Design</text>
    <text class="strong" x="154" y="523">Thinking in</text>
    <text class="strong" x="154" y="539">Organization</text>
    <text class="cap-label" x="48" y="335">CAP</text>
    <line x1="78" y1="331" x2="157" y2="331" stroke="var(--navy)" stroke-width="1.5" marker-end="url(#tip-navy)"/>
  </g>

  <!-- Research approach: RtD triangle -->
  <g class="approach">
    <text class="rtd" x="382" y="205">RtD</text>
    <text class="dimension" x="382" y="243">Learning Dimension</text>
    <text class="dimension" x="382" y="257">Pragmatic Dimension</text>
    <line x1="256" y1="269" x2="507" y2="269" stroke="var(--navy)" stroke-width="1.5" marker-start="url(#tip-navy)" marker-end="url(#tip-navy)"/>
    <polygon points="253,290 511,290 382,489" fill="var(--panel)"/>
    <polygon points="382,290 317,389 446,389" fill="var(--white)"/>
    <text class="lead" x="317" y="313">Design</text>
    <text class="strong" x="317" y="327">Practice</text>
    <text class="lead" x="446" y="313">Design</text>
    <text class="strong" x="446" y="327">Studies</text>
    <text class="lead" x="382" y="410">Design</text>
    <text class="strong" x="382" y="424">Exploration</text>
  </g>

  <!-- Brace -->
  <path d="M514 90 Q541 90 541 120 L541 320 Q541 345 564 345 Q541 345 541 370 L541 570 Q541 601 514 601" fill="none" stroke="var(--accent)" stroke-width="1.5"/>

  <!-- Methods column -->
  <g class="methods">
    <rect x="589" y="134" width="131" height="452" rx="8" fill="var(--panel)"/>
    <line class="divider" x1="589" y1="209" x2="720" y2="209"/>
    <line class="divider" x1="589" y1="285" x2="720" y2="285"/>
    <line class="divider" x1="589" y1="360" x2="720" y2="360"/>
    <line class="divider" x1="589" y1="435" x2="720" y2="435"/>
    <line class="divider" x1="589" y1="511" x2="720" y2="511"/>
    <text class="cell-text" x="654" y="167">Interventions</text>
    <text class="cell-text" x="654" y="182">Design</text>
    <text class="cell-text" x="654" y="243">Reflection</text>
    <text class="cell-text" x="654" y="258">on Action</text>
    <text class="cell-text" x="654" y="306">Reflective</text>
    <text class="cell-text" x="654" y="320">Conversation with</text>
    <text class="cell-text" x="654" y="335">the situation</text>
    <text class="cell-note" x="654" y="348">(Reflection in Action)</text>
    <text class="cell-text" x="654" y="401">Proto-Practices</text>
    <text class="cell-text" x="654" y="476">Interviews</text>
    <text class="cell-text" x="654" y="551">Observations</text>
  </g>

  <!-- Findings column -->
  <g class="findings">
    <rect x="799" y="134" width="131" height="452" rx="8" fill="var(--panel)"/>
    <line class="divider" x1="799" y1="248" x2="930" y2="248"/>
    <line class="divider" x1="799" y1="360" x2="930" y2="360"/>
    <line class="divider" x1="799" y1="473" x2="930" y2="473"/>
    <text class="cell-text" x="865" y="172">The Value of</text>
    <text class="cell-text" x="865" y="186">Semi-Structured</text>
    <text class="cell-text" x="865" y="201">Tools for</text>
    <text class="cell-text" x="865" y="215">Non-Designers</text>
    <text class="cell-text" x="865" y="267">Openness</text>
    <text class="cell-text" x="865" y="284">as a type of</text>
    <text class="cell-text" x="865" y="300">Mindset</text>
    <text class="cell-text" x="865" y="316">Supporting</text>
    <text class="cell-text" x="865" y="332">Competence</text>
    <text class="cell-text" x="865" y="348">Building</text>
    <text class="cell-text" x="865" y="405">The Importance</text>
    <text class="cell-text" x="865" y="419">of</text>
    <text class="cell-text" x="865" y="434">Insiders / Experts</text>
    <text class="cell-text" x="865" y="517">The Role of Time</text>
    <text class="cell-text" x="865" y="531">during &amp; between</text>
    <text class="cell-text" x="865" y="546">Design Activities</text>
  </g>

  <!-- Contribution column -->
  <g class="contribution">
    <rect x="1012" y="134" width="131" height="452" rx="8" fill="var(--panel)"/>
    <line class="divider" x1="1012" y1="284" x2="1143" y2="284"/>
    <line class="divider" x1="1012" y1="487" x2="1143" y2="487"/>
    <text class="cell-text" x="1077" y="188">Semi-Structured</text>
    <text class="cell-text" x="1077" y="203">and</text>
    <text class="cell-text" x="1077" y="217">Visual Design Tools</text>
    <text class="paper-ref" x="1077" y="237">(Paper 1-4)</text>
    <text class="cell-text" x="1077" y="327">Framework of</text>
    <text class="cell-text" x="1077" y="341">3 Core Concepts</text>
    <text class="cell-text" x="1077" y="365">Dialogocal Space</text>
    <text class="paper-ref" x="1077" y="381">(Paper 6)</text>
    <text class="cell-text" x="1077" y="402">Temporality</text>
    <text class="paper-ref" x="1077" y="419">(Paper 6)</text>
    <text class="cell-text" x="1077" y="443">Openness</text>
    <text class="paper-ref" x="1077" y="459">(Paper 5)</text>
    <text class="cell-text" x="1077" y="528">Guidelines</text>
    <text class="paper-ref" x="1077" y="548">(Paper 7)</text>
  </g>

  <!-- Links: methods to findings -->
  <g class="links">
    <path class="link" stroke="var(--pink)" d="M719 174 H765 Q768 174 768 177 V185 Q768 188 771 188 H798" marker-end="url(#tip-pink)"/>
    <path class="link" stroke="var(--green)" d="M719 249 H754 V200 Q754 197 757 197 H798" marker-end="url(#tip-green)"/>
    <path class="link" stroke="var(--green)" d="M754 249 V302 Q754 305 757 305 H798" marker-end="url(#tip-green)"/>
    <path class="link" stroke="var(--green)" d="M754 305 V419 Q754 422 757 422 H798" marker-end="url(#tip-green)"/>
    <path class="link" stroke="var(--green)" d="M754 422 V523 Q754 526 757 526 H798" marker-end="url(#tip-green)"/>
    <path class="link" stroke="var(--orange)" d="M719 324 H735 Q738 324 738 321 V209 Q738 206 741 206 H798" marker-end="url(#tip-orange)"/>
    <path class="link" stroke="var(--sky)" d="M719 398 H743 Q746 398 746 395 V217 Q746 214 749 214 H798" marker-end="url(#tip-sky)"/>
    <path class="link" stroke="var(--purple)" d="M719 473 H760 Q763 473 763 470 V317 Q763 314 766 314 H798" marker-end="url(#tip-purple)"/>
    <path class="link" stroke="var(--purple)" d="M763 433 Q763 430 766 430 H798" marker-end="url(#tip-purple)"/>
    <path class="link" stroke="var(--periwinkle)" d="M719 548 H772 Q775 548 775 545 V538 Q775 535 778 535 H798" marker-end="url(#tip-periwinkle)"/>

    <!-- Links: findings to contribution -->
    <path class="link" stroke="var(--pink)" d="M930 200 H978 Q981 200 981 203 V211 Q981 214 984 214 H1011" marker-end="url(#tip-pink)"/>
    <path class="link" stroke="var(--green)" d="M930 304 H963 Q966 304 966 301 V226 Q966 223 969 223 H1011" marker-end="url(#tip-green)"/>
    <path class="link" stroke="var(--green)" d="M966 304 V377 Q966 380 969 380 H1011" marker-end="url(#tip-green)"/>
    <path class="link" stroke="var(--periwinkle)" d="M930 419 H983 Q986 419 986 422 V525 Q986 528 989 528 H1011" marker-end="url(#tip-periwinkle)"/>
    <path class="link" stroke="var(--purple)" d="M930 529 H971 Q974 529 974 526 V394 Q974 391 977 391 H1011" marker-end="url(#tip-purple)"/>
    <path class="link" stroke="var(--purple)" d="M974 529 V541 Q974 544 977 544 H1011" marker-end="url(#tip-purple)"/>

    <!-- Connection dots -->
    <circle class="dot" cx="719" cy="174" r="6" fill="var(--pink)"/>
    <circle class="dot" cx="719" cy="249" r="6" fill="var(--green)"/>
    <circle class="dot" cx="719" cy="324" r="6" fill="var(--orange)"/>
    <circle class="dot" cx="719" cy="398" r="6" fill="var(--sky)"/>
    <circle class="dot" cx="719" cy="473" r="6" fill="var(--purple)"/>
    <circle class="dot" cx="719" cy="548" r="6" fill="var(--periwinkle)"/>
    <circle class="dot" cx="930" cy="200" r="6" fill="var(--pink)"/>
    <circle class="dot" cx="930" cy="304" r="6" fill="var(--green)"/>
    <circle class="dot" cx="930" cy="419" r="6" fill="var(--periwinkle)"/>
    <circle class="dot" cx="930" cy="529" r="6" fill="var(--purple)"/>
  </g>
</svg>
</body>
</html>
```